Ridgely Forge business card for handing simple contact information and generating service awareness

Utilizing the attached logo(s), generate a professional, but approachable, card conveying a sense of capability and integrity. Please only use one logo of the four attached; the different colors are all acceptable, but preference will be given to a design integrating a teal/turquoise logo,

I do not know where to put in the contact information or details?

Target Market(s)

Agriculture, Farming, Timber, Forestry, Construction, Crane Service

Industry/Entity Type

Contact Information for Business Card

Name, Phone Number, email address

Colors

Designer to choose colors to be used in the design.

Requirements
Nice to have
• It would be great to have either a mountain or one of the attached cranes as a backdrop on the rear of the card. Simple watermarks and/or Debossing is also great

```html
<!DOCTYPE html>
<html lang="en">
<head>
<meta charset="utf-8">
<title>Ridgely Forge – Business Card</title>
<link href="https://fonts.googleapis.com/css2?family=Arimo:wght@400;700&display=swap" rel="stylesheet">
<style>
  :root {
    --teal: #2e6e63;
    --white: #ffffff;
    --ink: #1d1d1d;
    --backdrop: #ebebed;
  }
  * { box-sizing: border-box; margin: 0; padding: 0; }
  html, body {
    width: 1200px;
    height: 1000px;
    overflow: hidden;
    background: var(--backdrop);
    font-family: "Arimo", Arial, sans-serif;
  }
  .canvas { position: relative; width: 1200px; height: 1000px; }

  .card {
    position: absolute;
    left: 303px;
    width: 593px;
    height: 338px;
  }
  .card--front { top: 108px; background: var(--white); }
  .card--back  { top: 553px; background: var(--teal); }

  /* Brand lockup */
  .brand {
    position: absolute;
    display: flex;
    flex-direction: column;
    align-items: center;
  }
  .brand__mark {
    width: 84px;
    height: 84px;
    border-radius: 50%;
    margin-bottom: 18px;
  }
  .brand__name {
    font-weight: 700;
    font-size: 27px;
    letter-spacing: 0.5px;
    white-space: nowrap;
  }
  .card--front .brand { left: 46px; width: 200px; top: 86px; }
  .card--front .brand__mark { background: var(--teal); }
  .card--front .brand__name { color: var(--teal); }

  .card--back .brand { left: 0; width: 100%; top: 52px; }
  .card--back .brand__mark { width: 100px; height: 100px; background: var(--white); margin-bottom: 22px; }
  .card--back .brand__name { color: var(--white); font-size: 36px; }

  /* Contact column */
  .contact {
    position: absolute;
    left: 275px;
    top: 85px;
    height: 170px;
    padding-left: 22px;
    border-left: 2px solid var(--teal);
  }
  .contact__accent {
    position: absolute;
    left: -2px;
    top: 0;
    width: 17px;
    height: 42px;
    background: var(--teal);
  }
  .contact__name {
    color: var(--teal);
    font-weight: 700;
    font-size: 26px;
    line-height: 1;
    margin-top: -3px;
  }
  .contact__role {
    color: var(--teal);
    font-size: 16px;
    margin-top: 4px;
  }
  .contact__phone {
    color: var(--ink);
    font-size: 18px;
    margin-top: 36px;
  }
  .contact__address {
    color: var(--ink);
    font-size: 14px;
    line-height: 1.25;
    margin-top: 12px;
  }
  .contact__email {
    color: var(--ink);
    font-size: 14px;
    margin-top: 9px;
  }

  .website {
    position: absolute;
    left: 0;
    width: 100%;
    top: 275px;
    text-align: center;
    color: var(--white);
    font-weight: 700;
    font-size: 17px;
  }
</style>
</head>
<body>
<main class="canvas">

  <section class="card card--front" aria-label="Business card front">
    <div class="brand">
      <span class="brand__mark" aria-hidden="true"></span>
      <span class="brand__name">Ridgely Forge</span>
    </div>

    <div class="contact">
      <span class="contact__accent" aria-hidden="true"></span>
      <p class="contact__name">SAMPLE NAME</p>
      <p class="contact__role">CEO/Founder</p>
      <p class="contact__phone">+123-456-7890</p>
      <p class="contact__address">123 Street Name, Suite 456<br>Country Name, State 78901</p>
      <p class="contact__email">samplename@ridgelyforge.com</p>
    </div>
  </section>

  <section class="card card--back" aria-label="Business card back">
    <div class="brand">
      <span class="brand__mark" aria-hidden="true"></span>
      <span class="brand__name">Ridgely Forge</span>
    </div>
    <p class="website">www.websitename.com</p>
  </section>

</main>
</body>
</html>
```